I need a business Card Design for my practice , i am clinical herbalist. I am a herbalist specializing in Lyme disease, autism, autoimmune diseases, difficult to cure diseasesDifficult to cure diseases. In my innovative practice i link traditional medicine, herbs with science, immunologu ,pharmacology.

Industry/Entity Type

Business

Contact Information for Business Card

My company name : OSRODEK ZIELNIKA
My name : Piotr Weltak
Name of my profession : Fitoterapeuta
In Polish language Fitoterapeuta is Herbalist .

e-mail: piotrweltak@osrodekzielnika.com
www.osrodek-zielnika.pl
phone : 574 806 215
My company adress : Dąbrowa Sękowska 14 , 38-415 Mielnik
I dont have logo .

Requirements
Nice to have
• My company

```html
<!DOCTYPE html>
<html lang="pl">
<head>
<meta charset="utf-8">
<title>Osrodek Zielnika – wizytówka</title>
<link rel="stylesheet" href="https://fonts.googleapis.com/css2?family=Open+Sans:wght@400;600&display=swap">
<style>
  :root {
    --page-bg: #ecebe8;
    --card-dark: #2f3031;
    --card-light: #ffffff;
    --brand-green: #4fb08f;
    --brand-brown: #6e5e5e;
    --text-dark: #2b2b2b;
    --faint-green: #e6f2ed;
  }
  * { box-sizing: border-box; margin: 0; padding: 0; }
  html, body { width: 1200px; height: 800px; overflow: hidden; }
  body {
    background: var(--page-bg);
    font-family: "Open Sans", Arial, sans-serif;
    position: relative;
  }
  .card {
    position: absolute;
    top: 250px;
    width: 520px;
    height: 300px;
    border-radius: 18px;
    box-shadow: 0 6px 18px rgba(0,0,0,0.15);
    overflow: hidden;
  }
  .card--front { left: 50px; background: var(--card-dark); }
  .card--back { left: 630px; background: var(--card-light); }

  .brand {
    position: absolute;
    display: flex;
    align-items: center;
    gap: 12px;
    font-weight: 400;
    letter-spacing: 0.12em;
    white-space: nowrap;
  }
  .brand__dot {
    border-radius: 50%;
    background: var(--brand-green);
    flex: none;
  }
  .card--front .brand {
    left: 50%; top: 50%;
    transform: translate(-50%, -50%);
    font-size: 26px;
    color: var(--brand-green);
  }
  .card--front .brand__dot { width: 30px; height: 30px; }

  .card--back .brand {
    left: 150px; top: 62px;
    font-size: 20px;
    color: var(--brand-brown);
  }
  .card--back .brand__dot { width: 22px; height: 22px; }

  .back-accent {
    position: absolute;
    right: -60px; top: -40px;
    width: 230px; height: 230px;
    border-radius: 50%;
    background: var(--faint-green);
  }

  .person {
    position: absolute;
    left: 0; top: 128px;
    border-left: 6px solid var(--brand-brown);
    padding-left: 14px;
  }
  .person__name { font-size: 22px; font-weight: 400; color: var(--text-dark); line-height: 1.1; }
  .person__role { font-size: 14px; color: var(--brand-green); }

  .contact {
    position: absolute;
    left: 28px; bottom: 22px;
    list-style: none;
    font-size: 13px;
    color: var(--text-dark);
  }
  .contact li { display: flex; align-items: center; gap: 10px; line-height: 1.75; }
  .contact svg { width: 13px; height: 13px; fill: var(--text-dark); flex: none; }

  .website {
    position: absolute;
    right: 24px; bottom: 118px;
    font-size: 13px;
    color: var(--brand-green);
  }
</style>
</head>
<body>
  <section class="card card--front" aria-label="Awers wizytówki">
    <div class="brand"><span class="brand__dot"></span>OSRODEK ZIELNIKA</div>
  </section>

  <section class="card card--back" aria-label="Rewers wizytówki">
    <div class="back-accent"></div>
    <div class="brand"><span class="brand__dot"></span>OSRODEK ZIELNIKA</div>

    <div class="person">
      <p class="person__name">Piotr Weltak</p>
      <p class="person__role">Fitoterapeuta</p>
    </div>

    <p class="website">www.osrodek-zielnika.pl</p>

    <ul class="contact">
      <li>
        <svg viewBox="0 0 16 16" aria-hidden="true"><path d="M1 5c0-2 3-3 7-3s7 1 7 3v1h-3V5H4v1H1zM4 7h8l2 6H2zm4 1.5a2 2 0 1 0 0 4a2 2 0 0 0 0-4z"/></svg>
        574 806 215
      </li>
      <li>
        <svg viewBox="0 0 16 16" aria-hidden="true"><path d="M1 3h14v10H1zm1.5 1.2L8 8.5l5.5-4.3z"/></svg>
        piotrweltak@osrodekzielnika.com
      </li>
      <li>
        <svg viewBox="0 0 16 16" aria-hidden="true"><path d="M8 1a5 5 0 0 0-5 5c0 4 5 9 5 9s5-5 5-9a5 5 0 0 0-5-5zm0 3a2 2 0 1 1 0 4a2 2 0 0 1 0-4z"/></svg>
        Dąbrowa Sękowska 14 , 38-415 Mielnik
      </li>
    </ul>
  </section>
</body>
</html>
```